'Ormel Property Development' Business Card

Business Card Features:

High Quality (potentially textured) thick card - preference is white textured card

Logo (supplied)

We plan to use the vertical logo as the main logo. But i am happy for people to use either if they find it works better for the design of the card.

The building icon and also the insert to the 'E' is in a metallic finish, i think this should be finished in a metallic embossed or raised style.
Updates

Please note i have attached both a horizontal and Vertical Logo for your reference. We plan to use the vertical logo as the main logo. But i am happy for people to use either if they find it works better for the design of the card.

Please note i am considering having the cards made on stainless steel. This introduces the option of having cut outs in the card and etching or printing for the design. If you have a good concept for this please submit.

http://www.tinquarry.example/black-metal-cards# this is a site that makes the metal cards to offer some direction . . . . Please note i am basic the selection o the best design, if that means normal print cards on paper then this is what i will choose. But there are some great options with the metal. Thanks.

Industry/Entity Type

Building

Requirements
Must have
• Helvetica font to details side of card - logo as supplied to opposite side.

Card Details:

Darrow Pketts
Managing Director

+61 487 263 518
+61 3 6172 4809

PO Box 73
Bentleigh, VIC 3024

darrow@ormel.example

www.ormel.example

```html
<!DOCTYPE html>
<html lang="en">
<head>
<meta charset="utf-8">
<title>Ormel Property Development – Business Card</title>
<link rel="stylesheet" href="https://fonts.googleapis.com/css2?family=Arimo:ital,wght@0,400;0,700;1,700&display=swap">
<style>
  :root {
    --backdrop: #9a9a98;
    --card-charcoal: #545554;
    --card-white: #f4f4f2;
    --panel-light: #e6e6e3;
    --text-light: #f2f2f0;
    --text-dark: #5a5b5a;
    --logo-silver: #ecece9;
    --font-main: "Arimo", "Helvetica Neue", Helvetica, Arial, sans-serif;
  }
  * { box-sizing: border-box; margin: 0; padding: 0; }
  html, body {
    width: 1200px; height: 1000px; overflow: hidden;
    background: var(--backdrop);
    font-family: var(--font-main);
  }
  .canvas { position: relative; width: 1200px; height: 1000px; }

  .card {
    position: absolute; left: 230px; width: 740px; height: 423px;
    background: var(--card-charcoal);
    overflow: hidden;
    box-shadow: 0 6px 18px rgba(0,0,0,0.25);
  }
  .card--front { top: 52px; }
  .card--back { top: 525px; }

  .rule { position: absolute; left: 0; background: var(--card-white); }

  /* Front */
  .front-logo {
    position: absolute; left: 0; right: 0; top: 112px;
    text-align: center; color: var(--logo-silver); font-weight: 700;
  }
  .front-logo__name { font-size: 92px; letter-spacing: 6px; line-height: 1; }
  .front-logo__tag { font-size: 19px; letter-spacing: 2px; margin-top: 12px; text-transform: uppercase; }
  .card--front .rule--upper { top: 336px; width: 100%; height: 5px; }
  .card--front .rule--lower { top: 398px; width: 100%; height: 4px; }

  /* Back */
  .card--back .rule--top { top: 50px; width: 500px; height: 2px; }
  .identity { position: absolute; left: 500px; top: 62px; color: var(--text-light); }
  .identity__name { font-size: 24px; font-weight: 700; font-style: italic; }
  .identity__role { font-size: 17px; margin-top: 4px; }

  .logo-panel {
    position: absolute; left: 0; top: 122px; width: 290px; height: 122px;
    background: var(--panel-light);
    display: flex; flex-direction: column; justify-content: center; padding-left: 40px;
    color: var(--text-dark); font-weight: 700;
  }
  .logo-panel__name { font-size: 50px; letter-spacing: 3px; line-height: 1; }
  .logo-panel__tag { font-size: 11.5px; letter-spacing: 1px; text-transform: uppercase; margin-top: 8px; }

  .card--back .rule--mid { top: 266px; width: 100%; height: 4px; }
  .website { position: absolute; left: 34px; top: 290px; color: var(--text-light); font-size: 17px; }

  .contact { position: absolute; left: 360px; top: 148px; color: var(--text-light); font-size: 17px; line-height: 1.3; }
  .contact__row { display: flex; margin-bottom: 10px; }
  .contact__label { width: 28px; }
  .contact__email { position: absolute; left: 340px; top: 338px; color: var(--text-light); font-size: 17px; }

  .card--back .rule--bottom { top: 380px; width: 100%; height: 5px; }
</style>
</head>
<body>
<main class="canvas">

  <section class="card card--front" aria-label="Business card, logo side">
    <div class="front-logo">
      <div class="front-logo__name">ORMEL</div>
      <div class="front-logo__tag">Property Development</div>
    </div>
    <div class="rule rule--upper"></div>
    <div class="rule rule--lower"></div>
  </section>

  <section class="card card--back" aria-label="Business card, details side">
    <div class="rule rule--top"></div>
    <div class="identity">
      <p class="identity__name">Darrow Pketts</p>
      <p class="identity__role">Managing Director</p>
    </div>

    <div class="logo-panel">
      <span class="logo-panel__name">ORMEL</span>
      <span class="logo-panel__tag">Property Development</span>
    </div>

    <div class="contact">
      <div class="contact__row"><span class="contact__label">A :</span><span>PO BOX 73 Bentleigh<br>VIC 3024</span></div>
      <div class="contact__row"><span class="contact__label">P :</span><span>0487263518<br>1800 614 207</span></div>
    </div>

    <div class="rule rule--mid"></div>
    <p class="website">W : www.ormel.example</p>
    <p class="contact__email">E : darrow@ormel.example</p>
    <div class="rule rule--bottom"></div>
  </section>

</main>
</body>
</html>
```